Memento Mori Calendar

I’m looking for a graphic designer to create a Memento Mori–style life calendar that captures the essence of OLVENTRA — minimal, timeless, and deeply philosophical.

The design should be black and white only, with a refined, clean aesthetic and a sense of stillness and precision.
It should feel modern yet eternal, reflecting the themes of time, mortality, and presence.

Deliverables (Print-Ready Files):

24 x 30 in

24 x 32 in

24 x 36 in

A1 (594 x 841 mm)

All formats should be high-resolution and ready for professional printing (300 DPI, CMYK).

Design Requirements:

The calendar layout should follow the Memento Mori life calendar concept (weeks of life represented as small squares or circles).

The overall tone: minimal, meditative, monochrome.

Include the brand name: OLVENTRA (in an elegant, understated placement).

Add the following quote at the bottom or in a subtle position:

“Life can only be understood backwards; but it must be lived forwards.”
— Henrik Vastmoe

Target Market(s)

The OLVENTRA audience consists of urban, creative individuals aged 25 to 45, belonging to a middle to upper-middle income class. They lead conscious, quietly ambitious lives, seeking balance between inner depth and modern design. Their values center on awareness, presence, authenticity, and emotional depth, reflected in their preference for a monochrome, minimal, and timeless aesthetic. They tend to be introverted, reflective, and spiritually curious, drawn to brands that embody meaning and restraint rather than excess. Their cultural and stylistic affinities include Pyrel, Tulve, Ni Ostra, The Quiet Bench Guild, Durvanne, and Ombrix — labels that share OLVENTRAs devotion to simplicity, substance, and subtle ritual.

Font styles to use
Serif
Sans Serif

Colors

Designer to choose only greyscale colors for use in the design.

Requirements
Must have
• The calendar layout should follow the Memento Mori life calendar concept (weeks of life represented as small squares or circles). The overall tone: minimal, meditative, monochrome. Include the brand name: qrnvalto (in an elegant, understated placement). Add the following quote at the bottom or in a subtle position: “Life can only be understood backwards; but it must be lived forwards.” — Henrik Vastmoe

```html
<!DOCTYPE html>
<html lang="en">
<head>
<meta charset="utf-8">
<title>Memento Mori — OLVENTRA Life Calendar</title>
<link rel="stylesheet" href="https://fonts.googleapis.com/css2?family=Montserrat:wght@300;400&display=swap">
<style>
  :root {
    --canvas: #ffffff;
    --paper: #f4f4f4;
    --band: #ebebeb;
    --ink: #111111;
    --line: #a0a0a0;
    --cell: #8a8a8a;
    --label: #8a8a8a;
  }
  * { margin: 0; padding: 0; box-sizing: border-box; }
  html, body {
    width: 1200px; height: 1200px; overflow: hidden;
    background: var(--canvas);
    font-family: "Montserrat", sans-serif;
  }
  .canvas { position: relative; width: 1200px; height: 1200px; }
  .poster {
    position: absolute; left: 250px; top: 64px;
    width: 719px; height: 1080px;
    background: var(--paper);
  }
  .poster__title {
    position: absolute; left: 47px; top: 28px;
    font-weight: 300; font-size: 34px; line-height: 36px;
    letter-spacing: 0.56em; color: var(--ink);
  }
  .poster__brand {
    position: absolute; right: 0; top: 37px;
    width: 152px; height: 16px;
    background: var(--band);
    font-weight: 400; font-size: 11px; line-height: 16px;
    letter-spacing: 0.3em; color: #333;
    padding-left: 25px; white-space: nowrap;
  }
  .poster__footer {
    position: absolute; left: 0; bottom: 0;
    width: 100%; height: 58px; background: var(--band);
  }
  .quote {
    position: absolute; right: 54px; top: 10px;
    text-align: right; font-size: 7px; line-height: 8.5px;
    color: #222; font-weight: 400; white-space: nowrap;
  }
  .calendar { position: absolute; left: 0; top: 0; }
  .calendar__ages text {
    font-family: "Montserrat", sans-serif; font-size: 6px; fill: var(--label);
  }
</style>
</head>
<body>
<div class="canvas">
  <div class="poster">
    <h1 class="poster__title">Memento<br>Mori</h1>
    <div class="poster__brand">OLVENTRA</div>
    <footer class="poster__footer">
      <p class="quote">“Life can only be understood backwards; but it must be lived forwards.”<br>— Henrik Vastmoe</p>
    </footer>
  </div>

  <svg class="calendar" width="1200" height="1200" viewBox="0 0 1200 1200" aria-label="Life calendar: 80 years of weeks">
    <defs>
      <g id="week-row" fill="none" stroke="var(--cell)" stroke-width="0.6">
        <rect x="0" y="0" width="6.6" height="6.6"/>
        <rect x="8.84" y="0" width="6.6" height="6.6"/>
        <rect x="17.68" y="0" width="6.6" height="6.6"/>
        <rect x="26.52" y="0" width="6.6" height="6.6"/>
        <rect x="35.36" y="0" width="6.6" height="6.6"/>
        <rect x="44.2" y="0" width="6.6" height="6.6"/>
        <rect x="53.04" y="0" width="6.6" height="6.6"/>
        <rect x="61.88" y="0" width="6.6" height="6.6"/>
        <rect x="70.72" y="0" width="6.6" height="6.6"/>
        <rect x="79.56" y="0" width="6.6" height="6.6"/>
        <rect x="88.4" y="0" width="6.6" height="6.6"/>
        <rect x="97.24" y="0" width="6.6" height="6.6"/>
        <rect x="106.08" y="0" width="6.6" height="6.6"/>
        <rect x="114.92" y="0" width="6.6" height="6.6"/>
        <rect x="123.76" y="0" width="6.6" height="6.6"/>
        <rect x="132.6" y="0" width="6.6" height="6.6"/>
        <rect x="141.44" y="0" width="6.6" height="6.6"/>
        <rect x="150.28" y="0" width="6.6" height="6.6"/>
        <rect x="159.12" y="0" width="6.6" height="6.6"/>
        <rect x="167.96" y="0" width="6.6" height="6.6"/>
        <rect x="176.8" y="0" width="6.6" height="6.6"/>
        <rect x="185.64" y="0" width="6.6" height="6.6"/>
        <rect x="194.48" y="0" width="6.6" height="6.6"/>
        <rect x="203.32" y="0" width="6.6" height="6.6"/>
        <rect x="212.16" y="0" width="6.6" height="6.6"/>
        <rect x="221" y="0" width="6.6" height="6.6"/>
      </g>
      <g id="week-block">
        <use href="#week-row" y="0"/>
        <use href="#week-row" y="8.85"/>
        <use href="#week-row" y="17.7"/>
        <use href="#week-row" y="26.55"/>
        <use href="#week-row" y="35.4"/>
        <use href="#week-row" y="44.25"/>
        <use href="#week-row" y="53.1"/>
        <use href="#week-row" y="61.95"/>
        <use href="#week-row" y="70.8"/>
        <use href="#week-row" y="79.65"/>
      </g>
      <g id="decade">
        <use href="#week-block" x="0"/>
        <use href="#week-block" x="303"/>
      </g>
    </defs>

    <g class="calendar__grid">
      <use href="#decade" transform="translate(344 174.4)"/>
      <use href="#decade" transform="translate(344 285.65)"/>
      <use href="#decade" transform="translate(344 396.9)"/>
      <use href="#decade" transform="translate(344 508.15)"/>
      <use href="#decade" transform="translate(344 619.4)"/>
      <use href="#decade" transform="translate(344 730.65)"/>
      <use href="#decade" transform="translate(344 841.9)"/>
      <use href="#decade" transform="translate(344 953.15)"/>
    </g>

    <g class="calendar__rules" stroke="var(--line)" stroke-width="0.6">
      <line x1="299.5" y1="174" x2="299.5" y2="1041"/>
      <line x1="609.5" y1="174" x2="609.5" y2="1041"/>
      <line x1="918" y1="174" x2="918" y2="1041"/>
      <line x1="299.5" y1="174" x2="309" y2="174"/>
      <line x1="299.5" y1="215" x2="309" y2="215"/>
      <line x1="299.5" y1="259" x2="309" y2="259"/>
      <line x1="299.5" y1="326.25" x2="309" y2="326.25"/>
      <line x1="299.5" y1="370.25" x2="309" y2="370.25"/>
      <line x1="299.5" y1="437.5" x2="309" y2="437.5"/>
      <line x1="299.5" y1="481.5" x2="309" y2="481.5"/>
      <line x1="299.5" y1="548.75" x2="309" y2="548.75"/>
      <line x1="299.5" y1="592.75" x2="309" y2="592.75"/>
      <line x1="299.5" y1="660" x2="309" y2="660"/>
      <line x1="299.5" y1="704" x2="309" y2="704"/>
      <line x1="299.5" y1="771.25" x2="309" y2="771.25"/>
      <line x1="299.5" y1="815.25" x2="309" y2="815.25"/>
      <line x1="299.5" y1="882.5" x2="309" y2="882.5"/>
      <line x1="299.5" y1="926.5" x2="309" y2="926.5"/>
      <line x1="299.5" y1="993.75" x2="309" y2="993.75"/>
      <line x1="299.5" y1="1037.75" x2="309" y2="1037.75"/>
    </g>

    <g class="calendar__ages">
      <text x="303.5" y="214.2">5</text>
      <text x="301" y="258.2">10</text>
      <text x="301" y="325.45">15</text>
      <text x="301" y="369.45">20</text>
      <text x="301" y="436.7">25</text>
      <text x="301" y="480.7">30</text>
      <text x="301" y="547.95">35</text>
      <text x="301" y="591.95">40</text>
      <text x="301" y="659.2">45</text>
      <text x="301" y="703.2">50</text>
      <text x="301" y="770.45">55</text>
      <text x="301" y="814.45">60</text>
      <text x="301" y="881.7">65</text>
      <text x="301" y="925.7">70</text>
      <text x="301" y="992.95">75</text>
      <text x="301" y="1036.95">80</text>
    </g>
  </svg>
</div>
</body>
</html>
```